Consulting firm needs a professional letterhead design

We need a professional letterhead design which is simple but unique. It should carry attributes of the latest designs in the market suitable for professional environmental consultancies.

- The logo is attached for you to USE.
- Our preferred color scheme is that shown in the logo.
- Letterhead text color is your choice to make.
- Logo to the left and text to the right plus slogan/tagline is desirable for this letterhead.

Use any address etc. of your choice in the letterhead.

Target Market(s)

Consulting firms and government agencies

Industry/Entity Type

Environmental Consultant

Colors
acd037
fece3e
85cae6
3277b5

Requirements
Must have
• Logo supplied and color scheme must be used.
Nice to have
• Nexa font is used in the Logo, so it would ne nice to have nexa font in the letterhead too.

```html
<!DOCTYPE html>
<html lang="en">
<head>
<meta charset="utf-8">
<title>Terravista Letterhead</title>
<link rel="stylesheet" href="https://fonts.googleapis.com/css2?family=Montserrat:wght@600&family=Open+Sans:wght@400&display=swap">
<style>
  :root {
    --stage: #e6e6e6;
    --paper: #ffffff;
    --ink: #2e3350;
    --yellow: #f6cc12;
    --orange: #f5921f;
    --lime: #a0cd4a;
    --green: #17a24a;
    --sky: #5ac8da;
    --teal: #1a86a6;
    --watermark: #f1f5ef;
    --phone-icon: #f29a1e;
    --fax-icon: #6cbd45;
    --web-icon: #3a8fc0;
  }
  * { margin: 0; padding: 0; box-sizing: border-box; }
  html, body {
    width: 1200px; height: 1200px; overflow: hidden;
    background: var(--stage);
  }
  .letterhead {
    position: absolute; left: 151px; top: 30px;
    width: 897px; height: 1140px;
    background: var(--paper);
    overflow: hidden;
  }
  .brand {
    position: absolute; left: 58px; top: 40px; width: 236px;
    text-align: center; color: var(--ink);
    font-family: "Montserrat", sans-serif; font-weight: 600;
  }
  .brand-mark {
    width: 78px; height: 78px; border-radius: 50%;
    margin: 4px auto 14px;
    background: var(--green);
  }
  .brand-name { font-size: 27px; letter-spacing: 1px; line-height: 1; white-space: nowrap; }
  .brand-tagline { font-size: 11.5px; line-height: 1.3; margin-top: 2px; white-space: nowrap; }
  .contact {
    position: absolute; left: 669px; top: 52px;
    font-family: "Open Sans", sans-serif; font-size: 12.5px; font-style: normal;
    color: var(--ink); line-height: 16px;
  }
  .contact-address { margin-bottom: 9px; white-space: nowrap; }
  .contact-line { display: flex; align-items: center; gap: 4px; height: 17.5px; white-space: nowrap; }
  .contact-line svg { width: 11px; height: 11px; flex: none; }
  .backdrop-mark {
    position: absolute; left: 220px; top: 332px;
    width: 460px; height: 460px; border-radius: 50%;
    background: var(--watermark);
  }
  .colour-bands {
    position: absolute; left: 0; bottom: 0; width: 897px; height: 30px;
  }
  .band { position: absolute; top: 0; height: 30px; }
  .band-sun { left: 0; width: 265px; background: linear-gradient(90deg, var(--yellow), var(--orange)); }
  .band-leaf { left: 269px; width: 348px; background: linear-gradient(90deg, var(--lime), var(--green)); }
  .band-water { left: 621px; width: 276px; background: linear-gradient(90deg, var(--sky), var(--teal)); }
</style>
</head>
<body>
  <main class="letterhead">
    <header>
      <div class="brand">
        <div class="brand-mark"></div>
        <div class="brand-name">TERRAVISTA</div>
        <div class="brand-tagline">Bridging research and sound policy</div>
      </div>
      <address class="contact">
        <div class="contact-address">2480 Harbour Lane, Suite 310<br>Millbrook, ON, K0L 2M0</div>
        <div class="contact-line">
          <svg viewBox="0 0 12 12"><path fill="var(--phone-icon)" d="M2.5 1l2 2.2-1 1.2c.7 1.5 1.8 2.6 3.1 3.2l1.2-1 2.2 2-1 1.4C5.5 9.8 2.2 6.5 1.1 2.2z"/></svg>
          <span>555-014-2207</span>
        </div>
        <div class="contact-line">
          <svg viewBox="0 0 12 12"><g fill="var(--fax-icon)"><rect x="3" y="1" width="6" height="3"/><rect x="1" y="4.5" width="10" height="4" rx="1"/><rect x="3" y="8" width="6" height="3"/></g></svg>
          <span>555-014-3391</span>
        </div>
        <div class="contact-line">
          <svg viewBox="0 0 12 12"><g fill="none" stroke="var(--web-icon)" stroke-width="1"><circle cx="6" cy="6" r="5"/><ellipse cx="6" cy="6" rx="2.2" ry="5"/><path d="M1 6h10M2 3.5h8M2 8.5h8"/></g></svg>
          <span>www.terravista-consult.com</span>
        </div>
      </address>
    </header>
    <div class="backdrop-mark" aria-hidden="true"></div>
    <footer class="colour-bands" aria-hidden="true">
      <div class="band band-sun"></div>
      <div class="band band-leaf"></div>
      <div class="band band-water"></div>
    </footer>
  </main>
</body>
</html>
```